Real Estate 24"x24" Sign, Business Card, Letter Head and Envelope

This is a 4 project contest. If we choose a design or designs we like from what you sent we are willing to pay an amount at our discretion for that design even if we don't like all your designs for the 4 projects. Please be creative. Attached are our logo files. Please message us with any questions. Thanks and Good Luck!
Project 1: QLTV Realty 24" x 24" yard sign
We want to use the same blue background in our logo for the sign where the logo in white font will be on. CMYK 100,80,0,0. Attached is a sample a local designer made for you to get an idea what we are looking for. In the sample, the website is way too big and the entire sign is very plain and not attractive looking plus blue color is wrong one. We want the logo on top as large as possible but keeping it proportionate and attractive looking buy not too big that it looks odd. The following information can go in white color background or same blue color background color. Our company colors are blue (as per logo), green (as per logo), and white. "Residential & Commercial" goes under the logo. Under that put our phone number "312-948-6051" as large as possible but still looks good and under that our website in much smaller but readable font "www.qltvrealty.com".
Project 2: Envelope
We have two version of the logo. Use one or both. Whatever looks best in your design. The envelope will be white. We only want on top left corner logo and underneath our mailing address: 5197 Larchmere Ave. Skokie, IL 60093-1725. Maybe some creative decorative design at bottom of envelope will look nice
Project 3: Letter Head
We have two version of the logo. Use one or both. Whatever looks best in your design. We want the following information on the top of the letterhead. Logo, address: 5197 Larchmere Ave., Skokie, IL 60093-1725, phone: 312-948-6051, fax: 312-682-9307 website www.qltvrealty.com, email: info@qltvrealty.com
Project 4: Business card
Use either logo. We need cards for two individuals. Information for Person 1: Dev Kulkarni, Managing Broker, Phone: 312-948-6051, Email: dev.kulkarni@qltvrealty.com. Person 2: Ajay Kulkarni Broker Phone: 312-519-8263 Email: ajay.kulkarni@qltvrealty.com. Add Address, Fax and website same as above letter head.

```html
<!DOCTYPE html>
<html lang="en">
<head>
<meta charset="utf-8">
<title>QLTV Realty Stationery</title>
<link href="https://fonts.googleapis.com/css2?family=Open+Sans:wght@400;600&display=swap" rel="stylesheet">
<style>
  :root {
    --bg: #e9eef5;
    --paper: #ffffff;
    --navy: #0c2566;
    --ink: #2b2b2b;
    --icon: #3a4a6b;
    --rule: #d6dae2;
    --faint-blue: #c9d3e6;
    --faint-green: #dfe8cf;
  }
  * { box-sizing: border-box; margin: 0; padding: 0; }
  html, body { width: 1200px; height: 1184px; overflow: hidden; }
  body {
    background: var(--bg);
    font-family: "Open Sans", sans-serif;
    color: var(--ink);
    position: relative;
  }

  /* Envelope */
  .envelope {
    position: absolute; left: 40px; top: 220px;
    width: 500px; height: 260px;
    background: var(--paper);
    box-shadow: 0 10px 30px rgba(20,40,80,.15);
  }
  .envelope__lining {
    position: absolute; left: 0; top: 0; width: 100%; height: 70px;
    background: var(--navy);
  }
  .envelope__flap-edge {
    position: absolute; left: 0; top: 70px; width: 100%; height: 1px;
    background: var(--rule);
  }
  .envelope__brand { position: absolute; left: 40px; top: 110px; }

  /* Brand name: one colour, one weight */
  .wordmark {
    display: flex; align-items: center; gap: 8px;
    font-family: "Open Sans", sans-serif; font-weight: 600;
    color: var(--ink); letter-spacing: .3px; line-height: 1;
  }
  .wordmark__square { width: 10px; height: 10px; background: var(--ink); }
  .envelope .wordmark { font-size: 26px; }

  /* Letterhead */
  .letterhead {
    position: absolute; left: 590px; top: 196px;
    width: 560px; height: 792px;
    background: var(--paper);
    box-shadow: 0 10px 30px rgba(20,40,80,.15);
    overflow: hidden;
  }
  .letterhead__brand { position: absolute; left: 48px; top: 56px; }
  .letterhead .wordmark { font-size: 30px; }
  .contact {
    position: absolute; right: 48px; top: 100px;
    text-align: right; font-size: 8.5px; line-height: 1.45; font-style: normal;
  }
  .contact__row { display: flex; justify-content: flex-end; align-items: center; gap: 5px; }
  .contact__icon { width: 8px; height: 8px; fill: var(--icon); }
  .contact__gap { height: 6px; }

  .letter { position: absolute; left: 48px; right: 48px; top: 200px; font-size: 9.5px; line-height: 1.35; }
  .letter__salutation { margin-bottom: 12px; }
  .letter__para { margin-bottom: 30px; }
  .letter__date { text-align: right; font-size: 8.5px; margin: -18px 0 18px; }
  .letter__list { margin-bottom: 34px; }
  .letter__closing { margin-bottom: 10px; }

  .signature {
    position: absolute; left: 48px; top: 580px; width: 130px; height: 52px;
    background: linear-gradient(90deg, #eceef2, #f6f7f9);
    border-radius: 4px;
  }
  .footer-art {
    position: absolute; left: 0; bottom: 0; width: 100%; height: 140px;
    background: linear-gradient(180deg, #ffffff 0%, var(--faint-blue) 60%, var(--faint-green) 100%);
    opacity: .7;
  }
</style>
</head>
<body>

<section class="envelope" aria-label="Envelope">
  <div class="envelope__lining"></div>
  <div class="envelope__flap-edge"></div>
  <div class="envelope__brand">
    <div class="wordmark"><span class="wordmark__square"></span>QLTV Realty</div>
  </div>
</section>

<section class="letterhead" aria-label="Letterhead">
  <div class="letterhead__brand">
    <div class="wordmark"><span class="wordmark__square"></span>QLTV Realty</div>
  </div>

  <address class="contact">
    <div>5197 Larchmere Ave.</div>
    <div>Skokie, IL 60093-1725</div>
    <div class="contact__gap"></div>
    <div class="contact__row">312-948-6051
      <svg class="contact__icon" viewBox="0 0 10 10"><path d="M2 0.5l2 2-1 1.2c.6 1.3 1.7 2.4 3 3l1.2-1 2 2L8 9.5C4 9.3.7 6 .5 2z"/></svg>
    </div>
    <div class="contact__row">312-682-9307
      <svg class="contact__icon" viewBox="0 0 10 10"><rect x="2" y="0.5" width="6" height="3"/><rect x="0.5" y="4" width="9" height="5" rx="1"/></svg>
    </div>
    <div class="contact__row">dev.kulkarni@qltvrealty.com
      <svg class="contact__icon" viewBox="0 0 10 10"><rect x="0.5" y="2" width="9" height="6" rx="1"/><path d="M1 2.5l4 3 4-3" stroke="#fff" fill="none"/></svg>
    </div>
    <div class="contact__row">www.qltvrealty.com
      <svg class="contact__icon" viewBox="0 0 10 10"><circle cx="5" cy="5" r="4.5"/><path d="M0.5 5h9M5 .5c-2 2.5-2 6.5 0 9M5 .5c2 2.5 2 6.5 0 9" stroke="#fff" fill="none" stroke-width=".7"/></svg>
    </div>
  </address>

  <div class="letter">
    <p class="letter__salutation">Lorem ipsum dolor</p>
    <p class="letter__para">Lorem ipsum dolor sit amet, consectetur adipiscing elit, sed do eiusmod tempor incididnt ut labore et dolore magna aliqua. Ut enim ad minim veniam, quis nostrud exercitation ullamco laboris nisi ut aliquip ex ea commdo consequat. Duis aute irure dolor in reprehenderit in voluptate velit esse cillum dolore eu fugiat nulla paritur. Excepteur sint occaecat cupidatat non proident, sunt in culpa qui officia des mollit anim id est labor.</p>
    <p class="letter__date">11.11.2018</p>
    <p class="letter__salutation">Lorem ipsum dolor</p>
    <p class="letter__para" style="margin-bottom:12px">Lorem ipsum dolor sit amet, consectetur adipiscing elit, sed do eiusmod tempor incididnt ut labore et dolore magna aliqua. Ut enim ad minim veniam, quis nostrud exercitation ullamco laboris nisi ut aliquip ex ea commdo consequat. Duis aute irure dolor in reprehenderit in voluptate velit esse cillum dolore eu fugiat nulla paritur. Excepteur sint occaecat cupidatat non proident, sunt in culpa qui officia des mollit anim id est labor.</p>
    <p class="letter__list">Lorem ipsum dolor sit amet<br>consectetur adipiscing elit<br>Lorem ipsum dolor<br>sed do eiusmod tempor incididunt ut labore et dolore magna aliqua<br>Ut enim ad minim veniam<br>Lorem ipsum dolor</p>
    <p class="letter__closing">Sincerely yours,</p>
  </div>

  <div class="signature" role="img" aria-label="Handwritten signature"></div>
  <div class="footer-art" role="img" aria-label="Faint decorative rooftop artwork"></div>
</section>

</body>
</html>
```